QUORVIX - Sydney Based Technology Consultancy -Logo & Business Card design

Who are we?
-
Quorvix is an emerging and advanced technology consulting and professional services business based in Sydney, Australia. Quorvix specialising in increasing value to organisations through the effective use of current and emerging technologies, ensuring that technology is a sustainable catalyst to attaining stated business goals.

We pride ourselves in challenging the norm.

What do we want?
-
We are looking to update our "Brand" we already have a simple “home grown” logo and we are now looking for a new one, once we have this updated logo and businesses look and feel though the business card design we will refresh our website with the new logo and design thus updating the Companies overall look at feel.

Our current site is www.quorvix-example.net.au is a very basic wordpress site and we will be updating it once we have the new logo and designs done

Our initial thoughts on the new Quorvix identity are
• Logo Concept
- One of the key things is obviously the 8
- I was thinking that a logo that had 8 as the core of the logo would be cool,
- Almost like having a “ring” or hoop that is twisted to form an 8 with different services scribed on the inside.
- So we would have a Large 8 and the inside would have ring each service or section engraved.

• Brand / web Feel
- Simple
- Professional
- Innovative
- Clear
- Destination
- Unique
- Impartial
- Safe
- Leading edge
- Familiar

- Emerging technologies
- White and ice / glacier blue
- The familiar feel of the Brindle web site
- Embedded specialist Video clips

• Portfolio of Services
- Quorvix – A smart place for Smart people
- Quorvix – we provide the process to take ideas from awareness to reality
- Focus should be on the brand quality consistent clear local knowledge with regional, national, theatre and global presence

Access to Specialists
- Emerging technologies
- Sustainability
- Collaboration
- Data centre
- Virtualisation

• Adjacent ideas under the one Brand
- Tembrosk – Enable Business Collaboration
- Plinsk – Infrastructure Virtualisation
- morvo - smart people and processes
- skandel - Emerging technologies
- brunhavel - business to technology integration
- tolpin - Smart Infrastructure
- yusk – Connected communities
- dwol - sustainability

Target Market(s)

Australia, New Zealand and Asia pacific organisations that are typically English speaking.
Markets
- IT & Technology partners
- Banking and Finance
- Health

Industry/Entity Type

Business

Requirements
Must have
• Logo
Business cards
Colour pallette
3D Logo
Nice to have
• Style guide
Designer who can also assist with new Wordpress design
Should not have
• we don't want cheap looking, overtly flashy or gimmicky logo.

```html
<!DOCTYPE html>
<html lang="en">
<head>
<meta charset="utf-8">
<title>Quorvix – Business Card &amp; Palette</title>
<link rel="stylesheet" href="https://fonts.googleapis.com/css2?family=Open+Sans:wght@400;600;700&display=swap">
<style>
  :root {
    --white: #fdfdfe;
    --ice: #ebf2f8;
    --glacier: #c4d5dc;
    --steel: #87949f;
    --mauve: #867d8e;
    --navy: #2f4266;
    --card-deep: #27354f;
    --frame: #b9cad3;
  }
  * { box-sizing: border-box; margin: 0; padding: 0; }
  html, body { width: 1200px; height: 845px; overflow: hidden; background: #fff; }
  body { position: relative; font-family: "Open Sans", Arial, sans-serif; }

  .card {
    position: absolute; top: 18px; width: 427px; height: 680px;
    border: 4px solid var(--frame);
    background:
      repeating-linear-gradient(90deg, rgba(255,255,255,0.025) 0 1px, transparent 1px 4px),
      var(--card-deep);
    color: var(--glacier);
    overflow: hidden;
  }
  .card--front { left: 25px; }
  .card--back { left: 567px; }

  .brand-name { position: absolute; font-weight: 700; color: var(--steel); letter-spacing: -1px; line-height: 1; white-space: nowrap; }
  .brand-dot { position: absolute; border-radius: 50%; background: var(--glacier); }

  .card--front .brand-name { left: 40px; top: 268px; font-size: 74px; }
  .card--front .brand-dot { left: 220px; top: 96px; width: 120px; height: 120px; opacity: 0.85; }

  .tagline-vertical {
    position: absolute; left: 382px; top: 440px; width: 380px;
    transform: rotate(-90deg); transform-origin: 0 0;
    font-size: 15px; color: var(--ice); white-space: nowrap;
  }
  .challenge { position: absolute; right: 18px; top: 462px; font-size: 22px; color: var(--white); white-space: nowrap; }
  .person { position: absolute; left: 0; width: 100%; text-align: center; top: 570px; padding-right: 14px; }
  .person-name { font-size: 27px; color: var(--glacier); line-height: 1.2; white-space: nowrap; }
  .person-role { font-size: 18px; color: var(--glacier); white-space: nowrap; }

  .card--back .brand-name { left: 0; width: 100%; text-align: center; top: 280px; font-size: 80px; color: transparent; -webkit-text-stroke: 1px var(--steel); }
  .card--back .brand-dot { left: 58px; top: 60px; width: 300px; height: 300px; background: rgba(135,148,159,0.08); }
  .back-statement {
    position: absolute; left: 70px; top: 160px; width: 280px; text-align: center;
    font-size: 14px; line-height: 1.6; color: rgba(135,148,159,0.75);
  }
  .contact { position: absolute; left: 0; width: 100%; top: 560px; text-align: center; font-size: 16px; line-height: 24px; color: var(--glacier); }
  .contact-row { white-space: nowrap; }
  .contact-row span + span { margin-left: 22px; }

  .palette { position: absolute; display: flex; flex-direction: column; }
  .palette--main { left: 476px; top: 385px; width: 64px; }
  .palette--mini { left: 1128px; top: 500px; width: 42px; }
  .swatch { display: flex; align-items: flex-end; font-size: 8px; color: #333; }
  .palette--main .swatch { height: 46px; padding: 0 0 12px 10px; }
  .palette--mini .swatch { height: 29px; padding: 0 0 8px 6px; font-size: 6px; }
  .swatch--white { background: var(--white); }
  .swatch--ice { background: var(--ice); }
  .swatch--glacier { background: var(--glacier); }
  .swatch--steel { background: var(--steel); }
  .swatch--mauve { background: var(--mauve); }
  .swatch--navy { background: var(--navy); color: #c4d5dc; }

  .logo-3d { position: absolute; left: 1002px; top: 500px; width: 190px; height: 180px; }
  .logo-3d .brand-name { left: 0; top: 118px; font-size: 44px; color: var(--steel); }
  .logo-3d .brand-dot { left: 30px; top: 0; width: 80px; height: 80px; background: var(--glacier); }

  .reflection { position: absolute; top: 704px; height: 141px; overflow: hidden; opacity: 0.55; }
  .reflection::after { content: ""; position: absolute; inset: 0; background: linear-gradient(to bottom, rgba(255,255,255,0) 0%, #fff 85%); }
  .reflection-inner { transform: scaleY(-1); text-align: center; color: var(--card-deep); }
  .reflection--front { left: 25px; width: 427px; }
  .reflection--back { left: 567px; width: 427px; }
  .reflection--palette { left: 476px; width: 64px; top: 740px; height: 60px; background: linear-gradient(var(--steel), var(--mauve)); opacity: 0.35; }
  .reflection--back .contact-row { font-size: 16px; line-height: 24px; }
</style>
</head>
<body>

  <section class="card card--front">
    <span class="brand-dot"></span>
    <span class="brand-name">Quorvix</span>
    <p class="tagline-vertical">Capturing Business Needs, Driving Business Outcome</p>
    <p class="challenge">Challenge Us!</p>
    <div class="person">
      <p class="person-name">Dale Harwick</p>
      <p class="person-role">Director Sales &amp; Marketing</p>
    </div>
  </section>

  <div class="palette palette--main">
    <div class="swatch swatch--white">#FDFDFE</div>
    <div class="swatch swatch--ice">#EBF2F8</div>
    <div class="swatch swatch--glacier">#C4D5DC</div>
    <div class="swatch swatch--steel">#87949F</div>
    <div class="swatch swatch--mauve">#867D8E</div>
    <div class="swatch swatch--navy">#2F4266</div>
  </div>

  <section class="card card--back">
    <span class="brand-dot"></span>
    <p class="back-statement">we are a dynamic group who understand where you and your market are headed and can provide the innovation that can set you apart from the pack.</p>
    <span class="brand-name">Quorvix</span>
    <div class="contact">
      <p class="contact-row">SUITE 14, 52 LARROW ST, SYDNEY, NSW 2000</p>
      <p class="contact-row"><span>T: (02) 5550 0142</span><span>F: (02) 5550 0187</span></p>
      <p class="contact-row">E: info@quorvix-example.net.au</p>
      <p class="contact-row">W: www.quorvix-example.net.au</p>
    </div>
  </section>

  <div class="logo-3d">
    <span class="brand-dot"></span>
    <span class="brand-name">Quorvix</span>
  </div>

  <div class="palette palette--mini">
    <div class="swatch swatch--ice">#EBF2F8</div>
    <div class="swatch swatch--glacier">#C4D5DC</div>
    <div class="swatch swatch--steel">#87949F</div>
  </div>

  <div class="reflection reflection--front" aria-hidden="true">
    <div class="reflection-inner">
      <p class="person-name">Dale Harwick</p>
      <p class="person-role">Director Sales &amp; Marketing</p>
    </div>
  </div>
  <div class="reflection reflection--palette" aria-hidden="true"></div>
  <div class="reflection reflection--back" aria-hidden="true">
    <div class="reflection-inner">
      <p class="contact-row">SUITE 14, 52 LARROW ST, SYDNEY, NSW 2000</p>
      <p class="contact-row">T: (02) 5550 0142 &nbsp; F: (02) 5550 0187</p>
      <p class="contact-row">E: info@quorvix-example.net.au</p>
      <p class="contact-row">W: www.quorvix-example.net.au</p>
    </div>
  </div>

</body>
</html>
```